Greek Yogurt Design

Design Brief – Premium Greek Yogurt Line (150g Pot)
Background
We are a small-to-medium dairy producer launching a new premium Greek yogurt range. This line will come in slightly larger pots than our standard yogurts, and we are targeting an upmarket clientele with a higher price point.
Product Details
Product: Greek Yogurt (fruit on the bottom, yogurt on top)
Flavours:
Natural
Strawberry
Forest Fruit
Peach & Apricot
Vanilla
Mango
Weight: 150g
Kosher Certification: 2 logos must be applied neatly (logos provided).
Lid: Standard universal lid (not flavour-specific).
Design Style
Clean, elegant, and premium feel (avoid clutter).
Should stand out as sophisticated compared to our standard range.
Visual hierarchy:
Brand & product type (Greek Yogurt) should be clear.
Flavour indicated with subtle but distinct cues (colour palette, fruit illustration/photography).
“Fruit on the bottom” message should be communicated simply.
Premium cues: minimalist typography, restrained colour palette, elegant fruit imagery.
References / Inspiration
Velmora Yogurt
– clean, bold, dairy-traditional.
Brask Dairy Greek Style
– natural, elegant design.
Lunaro Greek Yogurt
– modern, colourful yet clean.
Deliverables
Pot sleeve / pot design (to wrap around container).
Must work across all flavours with colour/flavour variation.
Space for universal lid (do not design individual lids).
Application of 2 kosher logos in a balanced way.
Updates
Industry/Entity Type
Dairy
Colors
Designer to choose colors to be used in the design.
Look and feel
Each slider illustrates characteristics of the customer's brand and the style your logo design should communicate.

```html
<!DOCTYPE html>
<html lang="en">
<head>
<meta charset="utf-8">
<title>Melkora Greek Yogurt – Pot Sleeves</title>
<link rel="stylesheet" href="https://fonts.googleapis.com/css2?family=Baloo+2:wght@700&family=Federo&family=Oswald:wght@300;400&display=swap">
<style>
  :root {
    --page: #f1f1f1;
    --cream: #f6efd9;
    --milk: #fbfaf5;
    --milk-shade: #e4e1d6;
    --strawberry: #e2223a;
    --strawberry-deep: #c51a30;
    --forest: #2e7a2c;
    --forest-deep: #24651f;
    --natural: #9a6a1f;
    --natural-deep: #845717;
    --badge: #ffffff;
    --badge-ring: #2a2a2a;
    --weight-text: #444444;
  }
  * { box-sizing: border-box; margin: 0; padding: 0; }
  html, body { width: 1200px; height: 716px; overflow: hidden; background: var(--page); }
  .sheet {
    width: 1200px; height: 716px;
    display: flex; flex-direction: column; align-items: center; justify-content: center;
  }
  .sleeve {
    position: relative; width: 416px; height: 239px; overflow: hidden;
    color: var(--cream);
  }
  .sleeve--strawberry { background: radial-gradient(circle at 50% 45%, var(--strawberry-deep) 0, var(--strawberry) 45%); }
  .sleeve--forest { background: radial-gradient(circle at 50% 45%, var(--forest-deep) 0, var(--forest) 45%); }
  .sleeve--natural { background: radial-gradient(circle at 50% 45%, var(--natural-deep) 0, var(--natural) 45%); }

  .brand {
    position: absolute; top: 24px; left: 0; width: 100%; text-align: center;
    font-family: "Baloo 2", system-ui, sans-serif; font-weight: 700; font-size: 22px; line-height: 1;
    color: var(--cream); white-space: nowrap;
  }
  .certs { position: absolute; left: 15px; top: 58px; display: flex; flex-direction: column; gap: 6px; }
  .cert {
    width: 38px; height: 38px; border-radius: 50%;
    background: var(--badge); border: 2px solid var(--badge-ring);
  }
  .product {
    position: absolute; left: 0; width: 100%; top: 86px; text-align: center;
    font-family: "Federo", Georgia, serif; font-weight: 400; font-size: 49px; line-height: 1;
    color: var(--cream); white-space: nowrap;
  }
  .product--with-note { top: 80px; }
  .product-note {
    position: absolute; left: 0; width: 100%; top: 132px; text-align: center;
    font-family: "Oswald", Arial, sans-serif; font-weight: 300; font-size: 12px; line-height: 1;
    letter-spacing: 0.5px; color: var(--cream); white-space: nowrap;
  }
  .cream-wave { position: absolute; left: 0; bottom: 0; width: 416px; height: 80px; }
  .flavour {
    position: absolute; left: 84px; width: 200px; text-align: center; z-index: 2;
    font-family: "Baloo 2", system-ui, sans-serif; font-weight: 700; font-size: 24px; line-height: 1;
    color: #fff; white-space: nowrap;
  }
  .flavour--with-note { top: 171px; }
  .flavour--solo { top: 193px; }
  .flavour-note {
    position: absolute; left: 84px; width: 200px; text-align: center; top: 200px; z-index: 2;
    font-family: "Oswald", Arial, sans-serif; font-weight: 300; font-size: 13px; line-height: 1;
    letter-spacing: 0.4px; color: #fff; white-space: nowrap;
  }
  .weight {
    position: absolute; left: 272px; top: 198px; z-index: 2;
    font-family: "Oswald", Arial, sans-serif; font-weight: 300; font-size: 9px; line-height: 1;
    color: var(--weight-text); white-space: nowrap;
  }
  .weight b { font-weight: 400; }
</style>
</head>
<body>
<main class="sheet">

  <section class="sleeve sleeve--strawberry" aria-label="Strawberry sleeve">
    <div class="brand">Melkora</div>
    <div class="certs"><span class="cert" aria-label="Kosher certification"></span><span class="cert" aria-label="Kosher certification"></span></div>
    <h2 class="product">Greek Yogurt</h2>
    <svg class="cream-wave" viewBox="0 0 416 80" role="img" aria-label="Milk splash wave">
      <defs><linearGradient id="milkA" x1="0" y1="0" x2="0" y2="1"><stop offset="0" stop-color="var(--milk)"/><stop offset="1" stop-color="var(--milk-shade)"/></linearGradient></defs>
      <path d="M0 28 C40 22 80 58 130 66 C180 72 230 70 255 50 C262 30 270 12 282 6 C300 18 320 40 345 42 C375 44 395 52 416 50 L416 80 L0 80 Z" fill="url(#milkA)"/>
    </svg>
    <div class="flavour flavour--with-note">Strawberry</div>
    <div class="flavour-note">FRUIT ON THE BOTTOM</div>
    <div class="weight">Nett W.<b>150g</b></div>
  </section>

  <section class="sleeve sleeve--forest" aria-label="Forest Fruit sleeve">
    <div class="brand">Melkora</div>
    <div class="certs"><span class="cert" aria-label="Kosher certification"></span><span class="cert" aria-label="Kosher certification"></span></div>
    <h2 class="product product--with-note">Greek Yogurt</h2>
    <p class="product-note">FRUIT ON THE BOTTOM</p>
    <svg class="cream-wave" viewBox="0 0 416 80" role="img" aria-label="Milk splash wave">
      <defs><linearGradient id="milkB" x1="0" y1="0" x2="0" y2="1"><stop offset="0" stop-color="var(--milk)"/><stop offset="1" stop-color="var(--milk-shade)"/></linearGradient></defs>
      <path d="M0 34 C40 28 80 60 130 68 C180 74 230 72 255 52 C262 30 270 12 282 6 C300 18 320 40 345 44 C375 48 395 56 416 54 L416 80 L0 80 Z" fill="url(#milkB)"/>
    </svg>
    <div class="flavour flavour--with-note">Forest Fruit</div>
    <div class="flavour-note">FRUIT ON THE BOTTOM</div>
  </section>

  <section class="sleeve sleeve--natural" aria-label="Natural sleeve">
    <div class="brand">Melkora</div>
    <div class="certs"><span class="cert" aria-label="Kosher certification"></span><span class="cert" aria-label="Kosher certification"></span></div>
    <h2 class="product">Greek Yogurt</h2>
    <svg class="cream-wave" viewBox="0 0 416 80" role="img" aria-label="Milk splash wave">
      <defs><linearGradient id="milkC" x1="0" y1="0" x2="0" y2="1"><stop offset="0" stop-color="var(--milk)"/><stop offset="1" stop-color="var(--milk-shade)"/></linearGradient></defs>
      <path d="M0 32 C40 26 80 62 130 70 C180 76 230 74 255 52 C262 30 270 12 282 6 C300 18 320 40 345 42 C375 44 395 52 416 50 L416 80 L0 80 Z" fill="url(#milkC)"/>
    </svg>
    <div class="flavour flavour--solo">Natural</div>
    <div class="weight">Nett W.<b>150g</b></div>
  </section>

</main>
</body>
</html>
```